Lantern & Plates Festival poster,rack card, business card

We need phase 1 of the 1st annual Lantern & Plates Festival to be held June 12 &13 2015. Location and etc to be given upon completion. We need a Poster design for store windows, a rack card for rack display, and a business size card to hand out to prospective exhibitors and attendees. The festival will focus on Food trucks and food vendors, along with multiple bands to play throughout the event . Additional work will be asked for after the phase one is complete, and we have more info such as sponsors and bands.

Attn all designers...... I opologize for the extreme delay on the project. I had an incendent that landed me in the hospital on sept 7, and I will not be released until next week ,at which time we will come to a decision. Thanks for your patience. Neil

```html
<!DOCTYPE html>
<html lang="en">
<head>
<meta charset="utf-8">
<title>Lantern &amp; Plates Festival Poster</title>
<link href="https://fonts.googleapis.com/css2?family=Bebas+Neue&family=Permanent+Marker&family=Oswald:wght@600&display=swap" rel="stylesheet">
<style>
  :root {
    --bg-top: #c24f2c;
    --bg-mid: #8e3532;
    --bg-bottom: #4a1d36;
    --gold: #f8c41c;
    --gold-deep: #e39a12;
    --gold-shadow: #9a4a14;
    --ribbon: #d9772c;
    --ribbon-dark: #a8501c;
    --ghost: rgba(52, 18, 40, 0.62);
    --speck: #f08a3a;
  }
  * { margin: 0; padding: 0; box-sizing: border-box; }
  html, body { width: 848px; height: 1200px; overflow: hidden; }
  body { background: var(--bg-bottom); }
  .poster {
    position: relative;
    width: 848px;
    height: 1200px;
    overflow: hidden;
    background:
      radial-gradient(ellipse 620px 520px at 42% 30%, rgba(230,110,50,0.55), transparent 70%),
      linear-gradient(180deg, var(--bg-top) 0%, var(--bg-mid) 45%, var(--bg-bottom) 100%);
  }
  .ghost-words {
    position: absolute;
    inset: 0;
    font-family: "Permanent Marker", cursive;
    color: var(--ghost);
    line-height: 1;
  }
  .ghost-words span { position: absolute; white-space: nowrap; }
  .ghost-beer  { left: -10px; top: 735px; font-size: 118px; transform: rotate(2deg); }
  .ghost-fun   { left: 600px; top: 715px; font-size: 120px; }
  .ghost-ohio  { left: -18px; top: 845px; font-size: 118px; }
  .ghost-year  { left: 650px; top: 820px; font-size: 110px; }
  .ghost-music { left: -25px; top: 955px; font-size: 150px; letter-spacing: -4px; }
  .ghost-fest  { left: 490px; top: 925px; font-size: 150px; letter-spacing: -4px; }
  .ghost-food  { left: -20px; top: 1075px; font-size: 150px; letter-spacing: -4px; }

  .notes span {
    position: absolute;
    color: var(--gold);
    text-shadow: 2px 3px 0 var(--gold-shadow), 4px 7px 8px rgba(40,10,20,0.5);
    font-family: serif;
    line-height: 1;
  }
  .title-block {
    position: absolute;
    left: 0; top: 0;
    width: 848px;
    transform: rotate(-3deg);
    transform-origin: 420px 400px;
  }
  .kicker {
    position: absolute;
    left: 250px; top: 205px;
    font-family: "Permanent Marker", cursive;
    font-size: 44px;
    color: var(--gold);
    letter-spacing: 1px;
    text-shadow: 2px 3px 0 var(--gold-shadow);
  }
  .headline {
    position: absolute;
    font-family: "Bebas Neue", sans-serif;
    color: var(--gold);
    line-height: 1;
    background: linear-gradient(180deg, #ffd43a 0%, var(--gold) 55%, var(--gold-deep) 100%);
    -webkit-background-clip: text;
    background-clip: text;
    -webkit-text-fill-color: transparent;
    filter: drop-shadow(3px 4px 0 var(--gold-shadow)) drop-shadow(8px 12px 10px rgba(40,10,20,0.55));
  }
  .headline-top { left: 200px; top: 272px; font-size: 150px; letter-spacing: 3px; }
  .headline-bottom { left: 300px; top: 420px; font-size: 150px; letter-spacing: 3px; }
  .headline-and {
    position: absolute;
    left: 165px; top: 480px;
    font-family: "Bebas Neue", sans-serif;
    font-size: 66px;
    color: var(--gold);
    text-shadow: 2px 3px 0 var(--gold-shadow);
  }
  .ribbon {
    position: absolute;
    left: 300px; top: 585px;
    width: 300px; height: 78px;
  }
  .ribbon-label {
    position: absolute;
    left: 300px; top: 596px;
    width: 300px;
    text-align: center;
    font-family: "Oswald", sans-serif;
    font-weight: 600;
    font-size: 36px;
    letter-spacing: 5px;
    color: var(--gold);
  }
  .location {
    position: absolute;
    left: 0; top: 695px;
    width: 900px;
    text-align: center;
    font-family: "Permanent Marker", cursive;
    font-size: 32px;
    line-height: 1.2;
    color: var(--gold);
    transform: rotate(-3deg);
  }
  .dates {
    position: absolute;
    left: 0; top: 845px;
    width: 920px;
    text-align: center;
    font-family: "Permanent Marker", cursive;
    font-size: 54px;
    color: #f8cf1c;
    transform: rotate(-3deg);
  }
</style>
</head>
<body>
<main class="poster">
  <div class="ghost-words" aria-hidden="true">
    <span class="ghost-beer">BEER</span>
    <span class="ghost-fun">FUN</span>
    <span class="ghost-ohio">OHIO</span>
    <span class="ghost-year">2015</span>
    <span class="ghost-music">MUSIC</span>
    <span class="ghost-fest">FEST</span>
    <span class="ghost-food">FOOD TRUCKS</span>
  </div>

  <div class="notes" aria-hidden="true">
    <span style="left:218px;top:140px;font-size:56px;transform:rotate(-12deg)">♫</span>
    <span style="left:410px;top:135px;font-size:52px;transform:rotate(-6deg)">♫</span>
    <span style="left:580px;top:150px;font-size:62px;transform:rotate(4deg)">♫</span>
    <span style="left:655px;top:222px;font-size:70px;transform:rotate(10deg)">♪</span>
    <span style="left:200px;top:560px;font-size:70px;transform:rotate(-14deg)">♪</span>
    <span style="left:640px;top:410px;font-size:52px">𝄞</span>
  </div>

  <div class="title-block">
    <p class="kicker">1ST ANNUAL</p>
    <h1>
      <span class="headline headline-top">LANTERN</span>
      <span class="headline-and">AND</span>
      <span class="headline headline-bottom">PLATES</span>
    </h1>
    <svg class="ribbon" viewBox="0 0 300 78" aria-hidden="true">
      <polygon points="8,20 292,4 286,50 14,66" fill="var(--ribbon)"/>
      <polygon points="14,66 286,50 282,58 18,74" fill="var(--ribbon-dark)"/>
    </svg>
    <p class="ribbon-label">FESTIVAL</p>
  </div>

  <p class="location">LOCATION WILL BE<br>SHOWN HERE</p>
  <p class="dates">JUNE 12–13</p>
</main>
</body>
</html>
```